Moving comapny Postcard mailer Design

I am looking for a 6x9 postcard with real images of our team. I would like to add the same review we currently have , I want the colors of the postcard to be orange and white. I want the team picture to be enlarged with the other pictures to be mimized. I will add example postcards to give rough ideas. My company is called Harlow Moving and the postcards with that name are our current postcards. The additional postcards are from other companies who have better postcards than mine. My goal is for my postcard to be better that theirs.

Target Market(s)

Wealthy people in the 35+ age group

Industry/Entity Type

Moving company

Requirements
Must have
• Beauty

```html
<!DOCTYPE html>
<html lang="en">
<head>
<meta charset="utf-8">
<title>Harlow Moving – Postcard Mailer</title>
<link rel="stylesheet" href="https://fonts.googleapis.com/css2?family=Poppins:ital,wght@0,400;0,600;0,700;0,800;0,900;1,400;1,900&display=swap">
<style>
  :root{
    --orange:#f39321;
    --blue:#2c67b3;
    --black:#0b0b0b;
    --white:#ffffff;
    --ink:#1d1d1f;
    --backdrop:#a9a9a9;
    --stamp:#b9babd;
    --coupon-shadow:#b5b5b5;
  }
  *{box-sizing:border-box;margin:0;padding:0}
  html,body{width:1200px;height:1117px;overflow:hidden}
  body{background:var(--backdrop);font-family:"Poppins",sans-serif;position:relative}

  .postcard{position:absolute;left:228px;width:744px;height:495px;overflow:hidden;
    background:linear-gradient(135deg,#f1f1f1 0%,#ffffff 45%,#ffffff 100%)}
  .postcard--front{top:53px}
  .postcard--back{top:573px}
  .postcard__art{position:absolute;inset:0;width:744px;height:495px}

  .headline{position:absolute;left:39px;font-weight:900;font-style:italic;line-height:1;letter-spacing:-1px;white-space:nowrap}
  .headline--brand{top:40px;font-size:50px;color:var(--orange)}
  .headline--main{top:88px;font-size:86px;color:var(--blue);letter-spacing:-2px}
  .headline--kicker{top:140px;font-size:38px;color:var(--orange)}
  .headline--kicker small{font-size:26px}
  .headline--simple{top:172px;font-size:86px;color:var(--blue);letter-spacing:-2px}

  .coupons{position:absolute;left:39px;display:flex;gap:12px}
  .postcard--front .coupons{top:177px}
  .postcard--back .coupons{top:326px}
  .coupon{width:119px;height:81px;background:var(--orange);color:var(--white);
    box-shadow:5px 4px 0 var(--coupon-shadow);position:relative;text-align:center;padding-top:6px}
  .coupon::before{content:"";position:absolute;inset:3px;border:1.5px dashed var(--white)}
  .coupon__amount{font-size:22px;font-weight:800;line-height:1.05;letter-spacing:-.5px}
  .coupon__rule{font-size:12px;font-weight:800;line-height:1.05}
  .coupon__note{font-size:7.5px;font-style:italic;margin-top:3px}

  .review{position:absolute;left:39px;top:288px;width:285px;font-size:9.8px;line-height:12.4px;font-style:italic;color:var(--ink);white-space:nowrap}
  .rating{position:absolute;left:39px;top:384px;display:flex;gap:3px}
  .rating svg{width:21px;height:21px;fill:var(--orange)}
  .dot-number{position:absolute;left:169px;top:387px;width:108px;height:21px;border:2px solid var(--blue);
    border-radius:11px;font-size:12px;font-weight:700;color:var(--ink);text-align:center;line-height:17px}

  .brandmark{position:absolute;display:flex;align-items:center;gap:8px;font-weight:800;color:var(--blue);white-space:nowrap}
  .postcard--front .brandmark{left:332px;top:318px;width:124px;flex-direction:column;font-size:16px}
  .brandmark__dot{width:26px;height:26px;border-radius:50%;background:var(--orange)}
  .postcard--back .brandmark{left:470px;top:58px;font-size:15px}

  .about{position:absolute;left:40px;top:255px;width:350px;font-size:10.4px;line-height:12px;color:var(--ink)}

  .stamp-box{position:absolute;left:635px;top:20px;width:85px;height:85px;background:var(--stamp)}

  .contact{position:absolute;top:452px;display:flex;align-items:center;gap:6px;color:var(--white);font-weight:700;font-size:20px;line-height:1;white-space:nowrap}
  .contact--phone{left:39px}
  .contact--web{left:260px;font-size:17px}
  .contact__icon{width:19px;height:19px;border-radius:50%;background:var(--orange);display:flex;align-items:center;justify-content:center}
  .contact__icon svg{width:11px;height:11px}
</style>
</head>
<body>

<section class="postcard postcard--front">
  <svg class="postcard__art" viewBox="0 0 744 495">
    <defs>
      <linearGradient id="teamTone" x1="0" y1="0" x2="0" y2="1">
        <stop offset="0" stop-color="#5d7a45"/><stop offset=".45" stop-color="#2b2d2f"/><stop offset="1" stop-color="#6d6d6d"/>
      </linearGradient>
      <linearGradient id="houseTone" x1="0" y1="0" x2="1" y2="1">
        <stop offset="0" stop-color="#8d8478"/><stop offset=".6" stop-color="#a9adb3"/><stop offset="1" stop-color="#5d7f3f"/>
      </linearGradient>
    </defs>
    <polygon role="img" aria-label="Photo: the moving crew posed in front of a box truck" points="449,0 744,0 744,290 489,327" fill="url(#teamTone)"/>
    <polygon role="img" aria-label="Photo: movers carrying wrapped furniture out of a house" points="494,334 744,298 744,495 521,495" fill="url(#houseTone)"/>
    <polygon points="408,0 431,0 478,430 474,430" fill="var(--blue)"/>
    <polygon points="437,0 441,0 521,495 485,495" fill="var(--orange)"/>
    <polygon points="0,425 222,430 236,495 0,495" fill="var(--blue)"/>
    <polygon points="233,432 511,436 519,495 241,495" fill="var(--black)"/>
  </svg>

  <div class="headline headline--brand">HARLOW</div>
  <div class="headline headline--main">MOVING</div>

  <div class="coupons">
    <div class="coupon"><div class="coupon__amount">$25 OFF</div><div class="coupon__rule">MOVES UNDER<br>$1000</div><div class="coupon__note">With this card</div></div>
    <div class="coupon"><div class="coupon__amount">$50 OFF</div><div class="coupon__rule">MOVES OVER<br>$1000</div><div class="coupon__note">With this card</div></div>
    <div class="coupon"><div class="coupon__amount">$100 OFF</div><div class="coupon__rule">MOVES OVER<br>$3000</div><div class="coupon__note">With this card</div></div>
  </div>

  <p class="review">"This company is incredible! After working all day, they<br>came to our house and without skipping a beat began<br>efficiently moving our heavy household items.<br>They had a great attitude, very friendly, and clearly<br>enjoyed working with each other! They took extremely<br>good care of my household items. Thank you for<br>a great experience!</p>

  <div class="rating" aria-label="Five stars">
    <svg viewBox="0 0 24 24"><path d="M12 1l3.2 7.2 7.8.7-5.9 5.2 1.8 7.7L12 17.8 5.1 21.8l1.8-7.7L1 8.9l7.8-.7z"/></svg>
    <svg viewBox="0 0 24 24"><path d="M12 1l3.2 7.2 7.8.7-5.9 5.2 1.8 7.7L12 17.8 5.1 21.8l1.8-7.7L1 8.9l7.8-.7z"/></svg>
    <svg viewBox="0 0 24 24"><path d="M12 1l3.2 7.2 7.8.7-5.9 5.2 1.8 7.7L12 17.8 5.1 21.8l1.8-7.7L1 8.9l7.8-.7z"/></svg>
    <svg viewBox="0 0 24 24"><path d="M12 1l3.2 7.2 7.8.7-5.9 5.2 1.8 7.7L12 17.8 5.1 21.8l1.8-7.7L1 8.9l7.8-.7z"/></svg>
    <svg viewBox="0 0 24 24"><path d="M12 1l3.2 7.2 7.8.7-5.9 5.2 1.8 7.7L12 17.8 5.1 21.8l1.8-7.7L1 8.9l7.8-.7z"/></svg>
  </div>
  <div class="dot-number">DOT#4810273</div>

  <div class="brandmark"><span class="brandmark__dot"></span>Harlow Moving</div>

  <div class="contact contact--phone">
    <span class="contact__icon"><svg viewBox="0 0 24 24"><path fill="#fff" d="M6.6 10.8a15.1 15.1 0 006.6 6.6l2.2-2.2a1 1 0 011-.25 11.4 11.4 0 003.6.6 1 1 0 011 1V20a1 1 0 01-1 1A17 17 0 013 4a1 1 0 011-1h3.5a1 1 0 011 1c0 1.250.2 2.450.6 3.6a1 1 0 01-.25 1z"/></svg></span>
    (555) 014-2290
  </div>
  <div class="contact contact--web">
    <span class="contact__icon"><svg viewBox="0 0 24 24" fill="none" stroke="#000" stroke-width="2"><circle cx="12" cy="12" r="9"/><path d="M3 12h18M12 3c3 3 3 15 0 18M12 3c-3 3-3 15 0 18"/></svg></span>
    www.harlowmovers.com
  </div>
</section>

<section class="postcard postcard--back">
  <svg class="postcard__art" viewBox="0 0 744 495">
    <defs>
      <linearGradient id="porchTone" x1="0" y1="0" x2="1" y2="1">
        <stop offset="0" stop-color="#6f8a55"/><stop offset=".5" stop-color="#2a2a2c"/><stop offset="1" stop-color="#9a9a8c"/>
      </linearGradient>
      <linearGradient id="garageTone" x1="0" y1="0" x2="1" y2="1">
        <stop offset="0" stop-color="#8a7d6c"/><stop offset=".5" stop-color="#2f4f6a"/><stop offset="1" stop-color="#6e8450"/>
      </linearGradient>
    </defs>
    <polygon role="img" aria-label="Photo: a crew member loading bins at the curb" points="0,0 191,0 211,129 0,129" fill="url(#porchTone)"/>
    <polygon role="img" aria-label="Photo: two movers carrying a wrapped sofa from a garage" points="197,0 379,0 397,129 218,129" fill="url(#garageTone)"/>
    <polygon points="383,0 405,0 455,448 451,448" fill="var(--blue)"/>
    <polygon points="413,0 417,0 484,437 466,437" fill="var(--orange)"/>
    <polygon points="0,425 222,430 236,495 0,495" fill="var(--blue)"/>
    <polygon points="233,432 511,436 519,495 241,495" fill="var(--black)"/>
  </svg>

  <div class="brandmark">Harlow Moving</div>
  <div class="stamp-box"></div>

  <div class="headline headline--kicker">MOVING <small>MADE</small></div>
  <div class="headline headline--simple">SIMPLE</div>

  <p class="about">For over ten years, our team at Harlow Moving has been providing Eastern Tennessee with unparalleled custom moving experience. We prioritize safety, timeliness, and communication to ensure our customers are happy and stress-free before, during, and after their move. No matter where you need to go, we're here to help!</p>

  <div class="coupons">
    <div class="coupon"><div class="coupon__amount">$25 OFF</div><div class="coupon__rule">MOVES UNDER<br>$1000</div><div class="coupon__note">With this card</div></div>
    <div class="coupon"><div class="coupon__amount">$50 OFF</div><div class="coupon__rule">MOVES OVER<br>$1000</div><div class="coupon__note">With this card</div></div>
    <div class="coupon"><div class="coupon__amount">$100 OFF</div><div class="coupon__rule">MOVES OVER<br>$3000</div><div class="coupon__note">With this card</div></div>
  </div>

  <div class="contact contact--phone">
    <span class="contact__icon"><svg viewBox="0 0 24 24"><path fill="#fff" d="M6.6 10.8a15.1 15.1 0 006.6 6.6l2.2-2.2a1 1 0 011-.25 11.4 11.4 0 003.6.6 1 1 0 011 1V20a1 1 0 01-1 1A17 17 0 013 4a1 1 0 011-1h3.5a1 1 0 011 1c0 1.250.2 2.450.6 3.6a1 1 0 01-.25 1z"/></svg></span>
    (555) 014-2290
  </div>
  <div class="contact contact--web">
    <span class="contact__icon"><svg viewBox="0 0 24 24" fill="none" stroke="#000" stroke-width="2"><circle cx="12" cy="12" r="9"/><path d="M3 12h18M12 3c3 3 3 15 0 18M12 3c-3 3-3 15 0 18"/></svg></span>
    www.harlowmovers.com
  </div>
</section>

</body>
</html>
```